E-Waste Recycling Company Business Card

New Electronic Recycling Company based in Long Island, New York called "Baron Rustwell" We take outdated computers, components, electrical wire, circuit breakers, ink cartridges, etc. We look mostly for donated items that we recycle for our customers but will pay for large quantities from businesses. The design should reflect that we are environmentally friendly and our unique Quadra Purge process that ensures all personal data is wiped clean off hard drives. Please use our attached logo
Electrical

```html
<!DOCTYPE html>
<html lang="en">
<head>
<meta charset="utf-8">
<title>Baron Rustwell – Business Card</title>
<link rel="stylesheet" href="https://fonts.googleapis.com/css2?family=Cinzel:wght@700&family=Roboto:wght@400&display=swap">
<style>
  :root {
    --canvas-bg: #e9e7e2;
    --card-white: #ffffff;
    --green: #5cc443;
    --green-light: #8fd866;
    --green-deep: #3fa52c;
    --ink: #3a3a3a;
    --ink-dark: #1f3a17;
    --white: #ffffff;
  }
  * { margin: 0; padding: 0; box-sizing: border-box; }
  html, body { width: 1200px; height: 1023px; overflow: hidden; }
  body { background: var(--canvas-bg); position: relative; font-family: "Roboto", sans-serif; }

  .card {
    position: absolute; left: 250px; width: 700px; height: 400px;
    border-radius: 4px; overflow: hidden;
    box-shadow: 0 6px 18px rgba(0,0,0,.18);
  }
  .card--front { top: 70px; background: var(--card-white); }
  .card--back {
    top: 550px;
    background: radial-gradient(ellipse at 30% 30%, var(--green-light) 0%, var(--green) 55%, var(--green-deep) 100%);
  }

  .swoosh { position: absolute; inset: 0; width: 100%; height: 100%; }

  .brand-mark {
    position: absolute; display: flex; align-items: center; gap: 10px; white-space: nowrap;
    font-family: "Cinzel", serif; font-weight: 700; font-size: 22px; color: var(--ink);
  }
  .brand-mark__dot { width: 26px; height: 26px; border-radius: 50%; background: var(--green); }
  .card--front .brand-mark { top: 30px; right: 130px; }
  .card--back .brand-mark { top: 150px; right: 40px; font-size: 24px; color: var(--white); }
  .card--back .brand-mark__dot { background: var(--white); width: 28px; height: 28px; }

  .company-name {
    position: absolute; left: 40px; top: 185px; white-space: nowrap;
    font-family: "Cinzel", serif; font-weight: 700; font-size: 24px; color: var(--green);
  }

  .person { position: absolute; left: 300px; top: 272px; }
  .person__name { font-family: "Cinzel", serif; font-weight: 700; font-size: 19px; color: var(--green); white-space: nowrap; }
  .person__role { font-size: 14px; color: var(--ink); margin-top: 2px; }

  .contacts { position: absolute; left: 300px; top: 322px; list-style: none; }
  .contacts li { display: flex; align-items: center; gap: 7px; font-size: 14.5px; color: var(--ink); line-height: 20px; white-space: nowrap; }
  .contacts svg { width: 13px; height: 13px; fill: var(--green); flex: none; }

  .address {
    position: absolute; right: 40px; top: 200px; text-align: left; font-style: normal;
    font-size: 15px; line-height: 21px; color: var(--ink);
  }

  .services {
    position: absolute; left: 20px; top: 140px; width: 340px; text-align: center;
    font-family: "Cinzel", serif; font-weight: 700; font-size: 17px; line-height: 27px; color: var(--white);
  }
  .services__lead { color: var(--ink-dark); }
</style>
</head>
<body>

<section class="card card--front" aria-label="Card front">
  <svg class="swoosh" viewBox="0 0 700 400" aria-hidden="true">
    <path d="M30 400 C150 300 380 140 700 60 L700 70 C420 160 220 300 120 400 Z" fill="var(--green)"/>
  </svg>

  <div class="brand-mark"><span class="brand-mark__dot"></span>Baron Rustwell</div>

  <div class="company-name">Baron Rustwell</div>

  <div class="person">
    <div class="person__name">Dana Marlowe</div>
    <div class="person__role">Director</div>
  </div>

  <ul class="contacts">
    <li><svg viewBox="0 0 16 16"><path d="M3 1h3l1.5 4-2 1.2a9 9 0 0 0 4.3 4.3L11 8.5l4 1.5v3a2 2 0 0 1-2 2A13 13 0 0 1 1 3a2 2 0 0 1 2-2z"/></svg>+1 555-014-7600</li>
    <li><svg viewBox="0 0 16 16"><path d="M1 3h14v10H1z M1 3l7 6 7-6" stroke="#fff" stroke-width="1.2"/></svg>hello@baronrustwell.net</li>
    <li><svg viewBox="0 0 16 16"><circle cx="8" cy="8" r="7"/><path d="M1 8h14M8 1c-3 4-3 10 0 14M8 1c3 4 3 10 0 14" stroke="#fff" stroke-width="1" fill="none"/></svg>www.baronrustwell.net</li>
  </ul>

  <address class="address">18 Alder Ln<br>Harbor Vale, New York</address>
</section>

<section class="card card--back" aria-label="Card back">
  <div class="brand-mark"><span class="brand-mark__dot"></span>Baron Rustwell</div>

  <p class="services">
    <span class="services__lead">We take outdated</span><br>
    Computers,<br>
    Components, Electrical Wire,<br>
    Circuit Breakers, Ink Cartridges
  </p>
</section>

</body>
</html>
```